Construction Company Business Card

We need a logo and a business card for our new construction company. We are based in Nairobi, Kenya. Our company specializes in the design and construction of high end residential homes and commercial buildings. We want a modern and elegant logo. Preferred colours are gun metal grey/ slate (or anything along those lines) and red as a feature. We are however open to any ideas. The design should communicate prestige and elegance in the work that we undertake.
The uploaded sketch is just something we were pondering with but you can completely disregard it.

Industry/Entity Type

Construction

Contact Information for Business Card

Company Name: Tabor Vask

Company Address:
Tabor Vask
P.O.Box 2871-00529
Ruaraka, Nairobi, 00529
Kenya

Name on business card: Tabor V. Osumba

```html
<!DOCTYPE html>
<html lang="en">
<head>
<meta charset="utf-8">
<title>Tabor Vask Construction – Business Card</title>
<link rel="stylesheet" href="https://fonts.googleapis.com/css2?family=Exo+2:wght@400;500;600&display=swap">
<style>
  :root {
    --page: #d9dadc;
    --card: #e6e5e3;
    --slate: #6f8396;
    --slate-dark: #5d6f80;
    --red: #ee2a2e;
    --ink-soft: #7d8c9b;
    --plan-light: #ebeae8;
    --plan-dark: #dcdcdc;
  }
  * { box-sizing: border-box; margin: 0; padding: 0; }
  html, body { width: 1200px; height: 900px; overflow: hidden; }
  body {
    background: var(--page);
    font-family: "Exo 2", "Trebuchet MS", sans-serif;
    position: relative;
  }
  .card {
    position: absolute;
    left: 300px;
    width: 600px;
    height: 343px;
    background: var(--card);
    box-shadow: 0 6px 18px rgba(0,0,0,0.18);
    overflow: hidden;
  }
  .card--front { top: 70px; }
  .card--back { top: 487px; }

  .band { position: absolute; bottom: 0; height: 16px; }
  .band--slate { left: 0; width: 63%; background: var(--slate); }
  .band--red { right: 0; width: 37%; background: var(--red); }

  .brand {
    display: flex;
    align-items: center;
    gap: 12px;
    color: var(--slate);
    font-weight: 600;
    letter-spacing: 0.04em;
    text-transform: uppercase;
  }
  .brand__square { width: 22px; height: 22px; background: var(--slate); }

  /* front */
  .card--front .brand {
    position: absolute;
    top: 118px;
    left: 0; right: 0;
    justify-content: center;
    font-size: 34px;
  }
  .tagline {
    position: absolute;
    right: 40px;
    bottom: 40px;
    color: var(--red);
    font-size: 15px;
  }

  /* back */
  .plan {
    position: absolute;
    inset: 0;
    background: linear-gradient(135deg, var(--plan-light) 0%, var(--plan-dark) 55%, var(--plan-light) 100%);
    opacity: 0.7;
  }
  .card--back .brand {
    position: absolute;
    top: 40px;
    left: 40px;
    font-size: 24px;
  }
  .card--back .band--slate { width: 50%; height: 16px; }
  .card--back .band--red { width: 50%; height: 22px; }
  .person { position: absolute; left: 40px; top: 160px; }
  .person__name { color: var(--red); font-size: 28px; font-weight: 500; }
  .person__role { color: var(--ink-soft); font-size: 14px; margin-top: 4px; margin-left: 12px; }
  .website {
    position: absolute;
    left: 62px;
    bottom: 42px;
    color: var(--red);
    font-size: 16px;
  }
  .contact {
    position: absolute;
    left: 330px;
    top: 118px;
    color: var(--ink-soft);
    font-size: 13.5px;
    line-height: 1.35;
  }
  .contact__row { display: flex; gap: 8px; }
  .contact__key { color: var(--red); width: 12px; }
  .address { margin-top: 16px; margin-left: 20px; }
</style>
</head>
<body>
  <section class="card card--front" aria-label="Card front">
    <div class="brand"><span class="brand__square"></span><span>Tabor Vask Construction</span></div>
    <p class="tagline">Quality you deserve and dependability you can count on</p>
    <div class="band band--slate"></div>
    <div class="band band--red"></div>
  </section>

  <section class="card card--back" aria-label="Card back">
    <div class="plan" role="img" aria-label="Faint architectural floor plan background"></div>
    <div class="brand"><span class="brand__square"></span><span>Tabor Vask Construction</span></div>
    <div class="person">
      <p class="person__name">Tabor V. Osumba</p>
      <p class="person__role">Job Title</p>
    </div>
    <div class="contact">
      <p class="contact__row"><span class="contact__key">M</span><span>+254 720418356</span></p>
      <p class="contact__row"><span class="contact__key">P</span><span>+61 412907345</span></p>
      <p class="contact__row"><span class="contact__key">E</span><span>tabor.v@taborvask.co.ke</span></p>
      <p class="address">P.O.Box 2871-00529 Ruaraka,<br>Nairobi, 00529 Kenya</p>
    </div>
    <p class="website">www.taborvask.co.ke</p>
    <div class="band band--slate"></div>
    <div class="band band--red"></div>
  </section>
</body>
</html>
```